Modern luxury trendy cosmetics label

Looking for a cosmetics packaging label design. We are looking for a professionel, modern and luxury look like Helena Voskuijl, Meadowfern Apothecary, Autumn Vale, Gordon Ellis Marsh, Quba, Oskar + Brandt, Velumo, Dizzy Walrus, the plainspoken, lumires de charme.Name of product: Alpine Edelweiss Wrap - No-Needle Contour Treatment Ingredients that have scientific proof of anti aging: Cherry blossom extact, collegen, hyaluronic acid, coconut oil. Color of product itself: Pastel pink. Smell: Cherry blossom. Colors of label: simple and black and white or some subtle colors.

Target Market(s)

Women, luxury market, modern women, young and old women

Industry/Entity Type

Cosmetics

Font styles to use
Sans Serif

Colors

Designer to choose colors to be used in the design.

Requirements
Must have
• A modern look, professional, cosmetics, beauty, professional market, original

```html
<!DOCTYPE html>
<html lang="en">
<head>
<meta charset="utf-8">
<title>Alpine Edelweiss Wrap – Label</title>
<link rel="stylesheet" href="https://fonts.googleapis.com/css2?family=Josefin+Sans:wght@300;400&family=Alegreya+Sans:wght@400&display=swap">
<style>
  :root {
    --page: #ffffff;
    --label: #fbeaf0;
    --band: #f8dbe3;
    --ink: #1a1a1a;
    --ink-soft: #3a3234;
    --bloom: #fde9ef;
    --shadow: rgba(40, 30, 35, 0.28);
  }
  html, body {
    margin: 0;
    padding: 0;
    width: 1067px;
    height: 1200px;
    overflow: hidden;
    background: var(--page);
  }
  .canvas {
    position: relative;
    width: 1067px;
    height: 1200px;
  }
  .label {
    position: absolute;
    left: 143px;
    top: 217px;
    width: 764px;
    height: 763px;
    background: var(--label);
    box-shadow: 0 22px 34px -6px var(--shadow), 0 2px 6px rgba(40, 30, 35, 0.12);
  }
  .brand {
    position: absolute;
    top: 52px;
    left: 0;
    width: 100%;
    margin: 0;
    text-align: center;
    font-family: "Josefin Sans", sans-serif;
    font-weight: 300;
    font-size: 104px;
    letter-spacing: 2px;
    color: var(--ink);
  }
  .title-band {
    position: absolute;
    top: 240px;
    left: 0;
    width: 763px;
    height: 270px;
    background: var(--band);
  }
  .blossom-art {
    position: absolute;
    left: 524px;
    top: 60px;
    width: 240px;
    height: 296px;
    background: radial-gradient(circle at 45% 40%, var(--bloom) 0%, rgba(253, 233, 239, 0) 70%);
  }
  .product-name {
    position: absolute;
    left: 54px;
    top: 52px;
    margin: 0;
    font-family: "Josefin Sans", sans-serif;
    font-weight: 400;
    color: var(--ink-soft);
    line-height: 1;
  }
  .product-name span { display: block; }
  .name-origin { font-size: 32px; letter-spacing: 4px; margin-bottom: 14px; }
  .name-main { font-size: 54px; letter-spacing: 3px; margin-bottom: 10px; }
  .name-type { font-size: 72px; letter-spacing: 3px; }
  .claim {
    position: absolute;
    left: 61px;
    top: 530px;
    margin: 0;
    font-family: "Alegreya Sans", sans-serif;
    font-size: 27px;
    line-height: 32px;
    color: var(--ink-soft);
  }
  .divider {
    position: absolute;
    left: 61px;
    top: 611px;
    width: 40px;
    height: 3px;
    background: var(--ink);
  }
  .ingredients {
    position: absolute;
    left: 61px;
    top: 627px;
    margin: 0;
    font-family: "Alegreya Sans", sans-serif;
    font-size: 20px;
    line-height: 29px;
    color: var(--ink-soft);
  }
</style>
</head>
<body>
<main class="canvas">
  <section class="label">
    <h1 class="brand">norvelle</h1>
    <div class="title-band">
      <h2 class="product-name">
        <span class="name-origin">ALPINE</span>
        <span class="name-main">EDELWEISS</span>
        <span class="name-type">WRAP</span>
      </h2>
    </div>
    <div class="blossom-art" role="img" aria-label="Outlined blossom flowers scattered across the right edge of the title band"></div>
    <p class="claim">No-Needle<br>Contour Treatment</p>
    <div class="divider"></div>
    <p class="ingredients">With Cherry Blossom Extact, Collegen,<br>Hyaluronic Acid, Coconut Oil</p>
  </section>
</main>
</body>
</html>
```